Postcard and Door Hanger Design

We need two pieces designed for marketing. Both will use the same logo and photo just the text will be slightly different. We need these designs looking very modern, clean, and simple while having the important information to stand out.

Postcard: 2 sided
- Side 1 just have large logo with our website and phone number
- Side 2 below.
- 4 x 6
- Use photo of house provided
- "Going Above and Beyond Every Time"
- "Call TODAY to Reserve your project by May 1st and receive 10% off"
- "Residential and Commercial"
- Our contact is 778-294-1175
- Website is www.velmarcoatings.com
- Might include something like "check out our portfolio on our website"

Use the above as a guidline and be creative with it, add or take away as you see fit as we are open to suggestions.

Door Hanger: 2 sided
Side 1 - Logo with contact details
Side 2 - Below
- 4 x 11
- "We are painting your neighborhood"
-"come see us in action at (then leave a space where we can stick a label onto our door hanger with an address of a home we are painting)
- Call today for a FREE ESTIMATE
- 778-294-1175
- www.velmarcoatings.com

Links:

https://www.filenook.net/sh/q3k8tz52rwa9pn/TR7XKLP-QZ

https://www.filenook.net/sh/xv6rr27jtl3wyd/HNwLRaPqTs

Logo File:

https://www.filenook.net/sh/p2d94hzb1wkq07/zfa-R9LKiv

```html
<!DOCTYPE html>
<html lang="en">
<head>
<meta charset="utf-8">
<title>Velmar Coatings – Door Hanger</title>
<link rel="stylesheet" href="https://fonts.googleapis.com/css2?family=Cinzel:wght@400&family=Marcellus&family=Open+Sans:wght@400&family=Crimson+Text:ital,wght@1,700&display=swap">
<style>
  :root {
    --backdrop: #3b3b3d;
    --paper: #ffffff;
    --slate: #464f5c;
    --teal: #00b0ad;
    --ink: #1f2a30;
    --sky: #6f9ccc;
    --lawn: #4d6a36;
    --kitchen: #6b5448;
  }
  * { box-sizing: border-box; margin: 0; padding: 0; }
  html, body { width: 900px; height: 1200px; overflow: hidden; }
  body { background: var(--backdrop); position: relative; font-family: "Open Sans", sans-serif; }

  .hanger { position: absolute; top: 60px; width: 408px; height: 1086px; background: var(--paper); }
  .hanger--front { left: 33px; }
  .hanger--back { left: 459px; }
  .hanger__face { position: absolute; left: 11px; top: 12px; width: 386px; height: 1062px; overflow: hidden; }
  .hanger--front .hanger__face { background: var(--slate); }
  .hanger--back .hanger__face { background: var(--teal); }

  .door-hole { position: absolute; left: 70px; top: 63px; width: 246px; height: 246px; border-radius: 50%; background: var(--paper); }

  .brand { position: absolute; left: 0; width: 100%; text-align: center; color: var(--paper); font-family: "Marcellus", serif; }
  .brand__mark { display: block; margin: 0 auto 38px; width: 58px; height: 58px; background: var(--teal); }
  .brand__name { display: block; font-size: 46px; letter-spacing: 4px; line-height: 1; }
  .brand__tag { display: block; font-size: 19px; letter-spacing: 15px; margin-top: 12px; padding-left: 15px; }
  .hanger--front .brand { top: 398px; }

  .photo { position: absolute; left: 0; width: 100%; }
  .photo--house { top: 625px; height: 306px; background: linear-gradient(180deg, var(--sky) 0%, #a9c1d8 28%, #5a6068 45%, var(--lawn) 70%, #6f8a4a 100%); }
  .photo--kitchen { top: 468px; height: 255px; background: linear-gradient(160deg, #d9d2c6 0%, #9b8a7a 40%, var(--kitchen) 70%, #3e302a 100%); }

  .contact { position: absolute; left: 0; width: 100%; text-align: center; color: var(--paper); font-family: "Marcellus", serif; }
  .contact__line { display: flex; align-items: center; justify-content: center; gap: 10px; }
  .contact svg { fill: var(--teal); flex: none; }
  .hanger--front .contact { top: 950px; }
  .hanger--front .contact__phone { font-size: 27px; letter-spacing: 2px; }
  .hanger--front .contact__web { font-size: 19px; margin-top: 8px; }

  .headline { position: absolute; left: 0; top: 350px; width: 100%; text-align: center; font-family: "Cinzel", serif; color: var(--ink); font-size: 34px; line-height: 35px; }
  .invite { position: absolute; left: 0; top: 736px; width: 100%; text-align: center; color: var(--ink); font-size: 12.5px; }
  .cta { position: absolute; left: 0; top: 904px; width: 100%; text-align: center; color: var(--ink); font-family: "Crimson Text", serif; font-style: italic; font-weight: 700; font-size: 16px; }
  .cta__accent { font-size: 19px; }

  .footer-band { position: absolute; left: 0; top: 938px; width: 100%; height: 124px; background: var(--slate); }
  .footer-brand { position: absolute; top: 18px; left: 0; width: 100%; display: flex; justify-content: center; align-items: center; gap: 12px; color: var(--paper); font-family: "Marcellus", serif; }
  .footer-brand__mark { width: 34px; height: 34px; background: var(--teal); }
  .footer-brand__text { display: flex; flex-direction: column; }
  .footer-brand__name { font-size: 24px; letter-spacing: 2px; line-height: 1; }
  .footer-brand__tag { font-size: 10px; letter-spacing: 8px; margin-top: 4px; }
  .footer-contact { position: absolute; top: 78px; left: 0; width: 100%; display: flex; justify-content: center; align-items: center; gap: 6px; color: var(--paper); font-family: "Marcellus", serif; font-size: 14px; }
  .footer-contact svg { fill: var(--teal); }
</style>
</head>
<body>

<section class="hanger hanger--front">
  <div class="hanger__face">
    <div class="door-hole"></div>
    <div class="brand">
      <span class="brand__mark"></span>
      <span class="brand__name">VELMAR</span>
      <span class="brand__tag">COATINGS</span>
    </div>
    <div class="photo photo--house" role="img" aria-label="Photo of a freshly painted grey two-storey house with a landscaped front garden under a blue sky"></div>
    <div class="contact">
      <div class="contact__line contact__phone">
        <svg width="18" height="22" viewBox="0 0 24 24"><path d="M6.6 10.8a15.1 15.1 0 0 0 6.6 6.6l2.2-2.2c.3-.3.7-.4 1-.2 1.1.4 2.3.6 3.6.6.6 0 1 .4 1 1V20c0 .6-.4 1-1 1A17 17 0 0 1 3 4c0-.6.4-1 1-1h3.5c.6 0 1 .4 1 1 0 1.3.2 2.5.6 3.6.1.3 0 .7-.2 1z"/></svg>
        <span>778-294-1175</span>
      </div>
      <div class="contact__line contact__web">
        <svg width="18" height="18" viewBox="0 0 24 24"><path d="M12 2a10 10 0 1 0 0 20 10 10 0 0 0 0-20zm6.9 6h-3a15.6 15.6 0 0 0-1.3-3.6A8 8 0 0 1 18.9 8zM12 4c.8 1.2 1.5 2.5 1.9 4h-3.8c.4-1.5 1.1-2.8 1.9-4zM4.3 14a8.2 8.2 0 0 1 0-4h3.4a16.5 16.5 0 0 0 0 4zm.8 2h3a15.6 15.6 0 0 0 1.3 3.6A8 8 0 0 1 5.1 16zm3-8h-3a8 8 0 0 1 4.3-3.6C8.8 5.5 8.4 6.7 8.1 8zM12 20c-.8-1.2-1.5-2.5-1.9-4h3.8c-.4 1.5-1.1 2.8-1.9 4zm2.3-6H9.7a14.7 14.7 0 0 1 0-4h4.6a14.7 14.7 0 0 1 0 4zm.3 5.6c.6-1.1 1-2.3 1.3-3.6h3a8 8 0 0 1-4.3 3.6zm1.7-5.6a16.5 16.5 0 0 0 0-4h3.4a8.2 8.2 0 0 1 0 4z"/></svg>
        <span>www.velmarcoatings.com</span>
      </div>
    </div>
  </div>
</section>

<section class="hanger hanger--back">
  <div class="hanger__face">
    <div class="door-hole"></div>
    <h1 class="headline">WE ARE<br>PAINTING YOUR<br>NEIGHBORHOOD</h1>
    <div class="photo photo--kitchen" role="img" aria-label="Photo of a modern kitchen interior with a dark wood island, bar stools and a coffered ceiling"></div>
    <p class="invite">come see us in action at</p>
    <p class="cta">Call today for a <span class="cta__accent">Free Estimate</span></p>
    <div class="footer-band">
      <div class="footer-brand">
        <span class="footer-brand__mark"></span>
        <span class="footer-brand__text">
          <span class="footer-brand__name">VELMAR</span>
          <span class="footer-brand__tag">COATINGS</span>
        </span>
      </div>
      <div class="footer-contact">
        <svg width="11" height="13" viewBox="0 0 24 24"><path d="M6.6 10.8a15.1 15.1 0 0 0 6.6 6.6l2.2-2.2c.3-.3.7-.4 1-.2 1.1.4 2.3.6 3.6.6.6 0 1 .4 1 1V20c0 .6-.4 1-1 1A17 17 0 0 1 3 4c0-.6.4-1 1-1h3.5c.6 0 1 .4 1 1 0 1.3.2 2.5.6 3.6.1.3 0 .7-.2 1z"/></svg>
        <span>778-294-1175</span>
        <svg width="10" height="10" viewBox="0 0 24 24"><circle cx="12" cy="12" r="10"/></svg>
        <span>www.velmarcoatings.com</span>
      </div>
    </div>
  </div>
</section>

</body>
</html>
```